Dentistry

Dentist's personal business card. No logo needed. The card shoul deliver the massage of reliability, professionalism, experience.
Please ad the full brief of the project: down the line it says: the winning look should be precise and pristine NO pictures of Teeth, smiles, instruments etc.

The details to be desplaid are:
Dr. Rob Valdoni
Doctor of Dental Surgery
PHD
Web. Www.drvaldoni.com
Email. Rob@drvaldoni.com
Tel 07731482590
Surgery address. 27Bharwick road London SW4 7QN UK
82 Fenwyn Row London SW3 2HT. Uk

Reason: Decided to make the payment unrefundable in order to get more designers involved.

Requirements
Should not have
• Logo, teeth, smile any sort of instruments.

```html
<!DOCTYPE html>
<html lang="en">
<head>
<meta charset="utf-8">
<title>Dr. Rob Valdoni – Business Card</title>
<link rel="stylesheet" href="https://fonts.googleapis.com/css2?family=Exo+2:wght@300;400;600&display=swap">
<style>
  :root {
    --navy: #16113a;
    --azure: #0080c8;
    --white: #ffffff;
  }
  html, body {
    margin: 0;
    padding: 0;
    width: 1200px;
    height: 804px;
    overflow: hidden;
    background: var(--navy);
  }
  .card {
    position: relative;
    width: 1200px;
    height: 804px;
    background: var(--navy);
    font-family: "Exo 2", sans-serif;
  }
  .identity {
    position: absolute;
    right: 400px;
    top: 330px;
    text-align: right;
  }
  .identity__name {
    margin: 0;
    color: var(--white);
    font-weight: 600;
    font-size: 60px;
    line-height: 1;
    letter-spacing: -0.5px;
  }
  .identity__degree {
    margin: 18px 0 0;
    color: var(--azure);
    font-weight: 300;
    font-size: 38px;
    line-height: 1;
  }
  .title-band {
    position: absolute;
    left: 39px;
    top: 534px;
    width: 1122px;
    height: 65px;
    background: var(--azure);
    display: flex;
    align-items: center;
    justify-content: center;
  }
  .title-band__text {
    margin: 0;
    color: var(--navy);
    font-weight: 400;
    font-size: 37px;
    letter-spacing: 1.5px;
    line-height: 1;
  }
</style>
</head>
<body>
  <main class="card">
    <div class="identity">
      <h1 class="identity__name">Dr. Rob Valdoni</h1>
      <p class="identity__degree">PHD</p>
    </div>
    <div class="title-band">
      <p class="title-band__text">DOCTOR OF DENTAL SURGERY</p>
    </div>
  </main>
</body>
</html>
```